ZESTORAMA Business Card Design

ZESTORAMA
Zestorama is a food van, serving high vibe delicious food to go. This business is dedicated to healthy delicious feel good food, beauty in service and a sustainable planet.

The van will operate in the south west of western Australia at music festivals events markets wherever people need great food to go!

I like the idea of vibrant green mixed with a yellow?? background with some rays like the sun through the background.
The font needs to say vibrant energetic
TO ME -vibrant energetic font has to appear to be on the move - perhaps with shading??

I like fusha if that works for font? but the colour has to say food too.

I would like a symbol on the card a simple V turned into a womans raised arms. This should be vibrant too.
Thank you
Blessings
Marisol

Target Market(s)

target lovers of healthy high vibe food. music festival goers. age 18- 50 feel. audiance conscious eaters of feel great food

Industry/Entity Type

Events

Contact Information for Business Card

ZESTORAMA
High Vibe Food
Van
Marisol -owner/opperator
0417385960
Face book symbol - ZESTORAMA

on the I would like a logo of a simple V turned into a womans arms up toward the sky flip side

My number and name again
Zestorama- feel great mobile food
Festivals, events, markets & where high vibe food 2 go is appreciated

Requirements
Nice to have
• Moving energetic font
colour that says high vibe and healthy food

a logo that is a simple V turned into a woman's raised arms in gratitude

```html
<!DOCTYPE html>
<html lang="en">
<head>
<meta charset="UTF-8">
<title>Zestorama Business Card</title>
<link href="https://fonts.googleapis.com/css2?family=Open+Sans:wght@400;600&display=swap" rel="stylesheet">
<style>
  :root {
    --page-bg: #e9e6e1;
    --card-black: #1f1f1f;
    --green-deep: #1ea84a;
    --green-mid: #39b54a;
    --lime: #b5d22c;
    --white: #ffffff;
  }
  * { margin: 0; padding: 0; box-sizing: border-box; }
  html, body {
    width: 1200px; height: 959px; overflow: hidden;
    background: var(--page-bg);
    font-family: "Open Sans", Arial, sans-serif;
  }
  .card {
    position: absolute; left: 100px; top: 195px;
    width: 1000px; height: 570px;
    background: var(--card-black);
    box-shadow: 0 18px 40px rgba(0,0,0,.25);
  }
  .top-band {
    position: absolute; left: 0; top: 0; width: 100%; height: 18px;
    display: flex; gap: 4px;
  }
  .top-band span {
    flex: 1;
    background: linear-gradient(90deg, var(--green-deep), var(--lime) 55%, var(--green-deep));
  }
  .brand-name {
    position: absolute; left: 60px; top: 100px;
    font-size: 50px; font-weight: 600; color: var(--green-mid);
    letter-spacing: .5px;
  }
  .person {
    position: absolute; left: 300px; top: 172px; width: 460px;
    text-align: center; color: var(--white);
  }
  .person-name { font-size: 38px; font-weight: 400; letter-spacing: .5px; }
  .person-title { font-size: 24px; font-weight: 400; margin-top: 4px; }
  .contact-tiles {
    position: absolute; left: 45px; right: 45px; bottom: 40px; height: 215px;
    display: flex; gap: 14px;
  }
  .tile {
    flex: 1;
    background: radial-gradient(ellipse at 60% 35%, var(--lime) 0%, var(--green-mid) 55%, var(--green-deep) 100%);
    color: var(--white);
    display: flex; flex-direction: column; align-items: center; justify-content: center;
    text-align: center; font-size: 18px; line-height: 1.5;
  }
  .tile-icon { width: 52px; height: 52px; margin-bottom: 14px; }
</style>
</head>
<body>
  <div class="card">
    <div class="top-band"><span></span><span></span><span></span></div>

    <div class="brand-name">Zestorama</div>

    <div class="person">
      <div class="person-name">DANIEL MORROW</div>
      <div class="person-title">GENERAL MANAGER</div>
    </div>

    <div class="contact-tiles">
      <div class="tile tile-phone">
        <svg class="tile-icon" viewBox="0 0 52 52" aria-hidden="true">
          <circle cx="26" cy="26" r="24" fill="var(--white)"/>
          <path d="M19 14c1.5-1 3-.5 3.8 1l2.2 4.5c.5 1.2 0 2.4-1 3l-1.6 1c1.2 3 3.5 5.5 6.6 7l1-1.6c.7-1 2-1.4 3-.9l4.5 2.2c1.4.8 1.9 2.3 1 3.8-1.3 2.4-4 3.6-6.6 2.8C23 33.9 17.8 28.7 15.5 21.5c-.8-2.6.8-5.9 3.5-7.5z" fill="var(--green-mid)"/>
        </svg>
        <div>001 482 615 937</div>
        <div>001 482 615 937</div>
      </div>
      <div class="tile tile-address">
        <svg class="tile-icon" viewBox="0 0 52 52" aria-hidden="true">
          <circle cx="26" cy="26" r="24" fill="var(--white)"/>
          <path d="M26 11c-6 0-10.5 4.5-10.5 10.3 0 7.5 10.5 19.7 10.5 19.7s10.5-12.2 10.5-19.7C36.5 15.5 32 11 26 11z" fill="var(--green-mid)"/>
          <circle cx="26" cy="21.5" r="4" fill="var(--white)"/>
        </svg>
        <div>Harbor Lane St.2718</div>
        <div>Maple City. Ottawa</div>
      </div>
      <div class="tile tile-web">
        <svg class="tile-icon" viewBox="0 0 52 52" aria-hidden="true">
          <circle cx="26" cy="26" r="24" fill="var(--white)"/>
          <g fill="none" stroke="var(--green-mid)" stroke-width="2.2">
            <circle cx="26" cy="26" r="14"/>
            <ellipse cx="26" cy="26" rx="6" ry="14"/>
            <line x1="12" y1="26" x2="40" y2="26"/>
            <line x1="14" y1="19" x2="38" y2="19"/>
            <line x1="14" y1="33" x2="38" y2="33"/>
          </g>
        </svg>
        <div>info@zestmail.com</div>
        <div>www.Zestoramafood.com</div>
      </div>
    </div>
  </div>
</body>
</html>
```